Lumo Brew Premium Matcha brand Label

This is a label design project for a luxury tea brand. Feel free to be creative within the guidelines.
Attached to this project is a document called “Private Label Design Requirements” with the design guidelines and template. There is another document called "Lumo Brew Packaging Instructions" this has more details necessary to stick to the guidelines in the first document.

I have also attached the certifications to be included as well as different variations of the logo for you to use.

If you have any questions, I am here.
Updates

Target Market(s)

Young, active, fun, enjoy the finer things

```html
<!DOCTYPE html>
<html lang="en">
<head>
<meta charset="utf-8">
<title>Lumo Brew Premium Ceremonial Matcha Label</title>
<link href="https://fonts.googleapis.com/css2?family=Raleway:wght@500;600;700&display=swap" rel="stylesheet">
<style>
  :root {
    --page-bg: #bfcab9;
    --label-bg: #323d35;
    --leaf-tone: #3a473e;
    --ink: #ffffff;
    --matcha: #7cc242;
    --badge-green: #1f7a3a;
    --badge-blue: #2b6fb3;
  }
  * { margin: 0; padding: 0; box-sizing: border-box; }
  html, body { width: 1200px; height: 803px; overflow: hidden; }
  body {
    background: var(--page-bg);
    font-family: "Raleway", sans-serif;
    color: var(--ink);
    position: relative;
  }
  .label {
    position: absolute;
    left: 51px; top: 294px;
    width: 1098px; height: 214px;
    background: var(--label-bg);
    overflow: hidden;
  }
  .leaf-pattern {
    position: absolute; inset: 0;
    background: radial-gradient(ellipse at 20% 40%, var(--leaf-tone) 0%, transparent 60%),
                radial-gradient(ellipse at 75% 70%, var(--leaf-tone) 0%, transparent 55%),
                var(--label-bg);
  }
  .distributor {
    position: absolute; left: 69px; top: 86px;
    font-size: 9.5px; font-weight: 700; line-height: 16px;
  }
  .emblem {
    position: absolute; left: 463px; top: 23px;
    width: 168px; height: 168px;
  }
  .emblem svg { position: absolute; inset: 0; }
  .emblem-mark {
    position: absolute; left: 75px; top: 42px;
    width: 18px; height: 18px; border-radius: 50%;
    background: var(--matcha);
  }
  .brand-name {
    position: absolute; left: 0; right: 0; top: 79px;
    text-align: center; font-size: 13px; font-weight: 700; line-height: 16px;
  }
  .product-title {
    position: absolute; left: 0; right: 0; top: 100px;
    text-align: center; font-size: 11px; font-weight: 700; line-height: 14.5px;
  }
  .net-weight {
    position: absolute; left: 0; right: 0; top: 136px;
    text-align: center; font-size: 7px; font-weight: 600; line-height: 9px;
  }
  .details { position: absolute; left: 783px; top: 41px; }
  .details h2 { font-size: 12px; font-weight: 600; line-height: 16px; }
  .ingredients { font-size: 9.5px; font-weight: 700; margin: 2px 0 0 9px; }
  .instructions-heading { margin-top: 9px; }
  .instructions { list-style: none; margin-left: 9px; font-size: 9px; font-weight: 700; line-height: 12px; }
  .instructions li::before { content: "• "; }
  .certifications {
    position: absolute; left: 921px; top: 143px;
    display: flex; align-items: center; gap: 5px;
  }
  .cert-circle {
    width: 32px; height: 32px; border-radius: 50%;
    background: var(--badge-green); border: 2px solid var(--ink);
  }
  .cert-square { width: 36px; height: 26px; background: var(--badge-blue); border: 2px solid var(--ink); }
</style>
</head>
<body>
  <section class="label">
    <div class="leaf-pattern" role="img" aria-label="Faint tea leaf pattern across the label background"></div>

    <div class="distributor">
      <p>Distributed by Lumo Brew Co. | Maple Falls, Ga</p>
      <p>Certified Organic by verdia</p>
      <p>PRODUCT OF JAPAN</p>
    </div>

    <div class="emblem">
      <svg viewBox="0 0 168 168" aria-hidden="true">
        <path class="ring-top" d="M11.2 102.1 A75 75 0 1 1 156.8 102.1" fill="none" stroke="#ffffff" stroke-width="18"/>
        <path class="ring-bottom" d="M140.6 133.2 A75 75 0 0 1 27.4 133.2" fill="none" stroke="#ffffff" stroke-width="18"/>
      </svg>
      <span class="emblem-mark"></span>
      <p class="brand-name">Lumo Brew</p>
      <h1 class="product-title">PREMIUM ORGANIC<br>CEREMONIAL MATCHA</h1>
      <p class="net-weight">Net Wt: 30g</p>
    </div>

    <div class="details">
      <h2>Ingredients</h2>
      <p class="ingredients">Premium Organic Japanese Matcha Green Tea</p>
      <h2 class="instructions-heading">Instructions</h2>
      <ul class="instructions">
        <li>2 tsp of Matcha</li>
        <li>2oz of Water (170-180 degrees F)</li>
        <li>Whisk in a W formation until frothy</li>
        <li>Sweeten to taste</li>
      </ul>
    </div>

    <div class="certifications">
      <span class="cert-circle" role="img" aria-label="Organic certification badge"></span>
      <span class="cert-square" role="img" aria-label="Non-GMO verification badge"></span>
    </div>
  </section>
</body>
</html>
```